Flyer Design For Tech Support Company

We need a flyer design for our company Corvalo Crafted Systems Ltd. I would like this to follow the same theme and styling of: www.corvalosys.co.uk I would also invite you to use any information as found on our site. I would like this to focues primarily on attracting small bussines/start-up new custom; additionaly if there could be a mention of being able to work with private customers also.

Target Market(s)

Start-up, Small Businnes, Private Home.

Industry/Entity Type

It Company

Font styles to use
Sans Serif

Colors
33a6d7

Requirements
Must have
• Follow theme/style of main site.
• Be bold to attract from a distance.
Should not have
• Funny's

```html
<!DOCTYPE html>
<html lang="en">
<head>
<meta charset="utf-8">
<title>Corvalo Crafted Systems – Support Flyer</title>
<link href="https://fonts.googleapis.com/css2?family=Open+Sans:ital,wght@0,400;0,600;0,700;1,400;1,600;1,700&display=swap" rel="stylesheet">
<style>
:root{
  --brand:#33a6d7;
  --brand-dark:#2a8fbb;
  --ink:#222;
  --ink-soft:#444;
  --paper:#fff;
  --night:#1d1f20;
  --stage:#e9eef0;
  --hero-a:#20424f;
  --hero-b:#3f6f7a;
}
*{margin:0;padding:0;box-sizing:border-box}
html,body{width:960px;height:1200px;overflow:hidden;background:var(--stage);font-family:"Open Sans",Arial,sans-serif;color:var(--ink)}
.sheet{position:absolute;top:270px;width:465px;height:659px;background:var(--paper);box-shadow:0 2px 10px rgba(0,0,0,.15);overflow:hidden}
.sheet--front{left:10px}
.sheet--back{left:485px}
.topbar{position:absolute;left:0;top:0;width:100%;height:28px;background:var(--brand);display:flex;align-items:center;gap:6px;padding-left:14px;color:#fff;font-size:7.5px}
.topbar svg{display:block}
.topbar .dot{width:7px;height:7px;border-radius:50%;background:#fff;margin-left:4px}
.footer{position:absolute;left:0;bottom:0;width:100%;height:20px;background:var(--brand);display:flex;align-items:center;justify-content:center;gap:8px;color:#fff;font-size:8px}
.footer .rule{flex:1;height:1px;background:#fff;margin:0 12px}
.footer .dot{width:6px;height:6px;border-radius:50%;background:#fff}
.sheet--back .footer{background:var(--paper);color:var(--brand)}
.sheet--back .footer .rule,.sheet--back .footer .dot{background:var(--brand)}

/* front */
.brand-card{position:absolute;left:174px;top:13px;width:116px;height:100px;background:#fff;border-radius:10px;z-index:2;display:flex;flex-direction:column;align-items:center;justify-content:center;gap:6px}
.brand-card .mark{width:22px;height:22px;border-radius:50%;background:var(--brand)}
.brand-name{color:var(--brand);font-weight:600;font-size:11px;text-align:center;line-height:1.15}
.hero{position:absolute;left:0;top:105px;width:100%;height:162px;background:linear-gradient(120deg,var(--hero-a),var(--hero-b) 60%,#5b7f7e)}
.hero__title{position:absolute;left:0;top:50px;width:100%;text-align:center;color:#fff;font-weight:700;font-size:15px;line-height:1.3}
.hero__tag{position:absolute;left:186px;top:98px;width:93px;height:28px;border:1.5px solid #fff;color:#fff;font-weight:700;font-size:15px;display:flex;align-items:center;justify-content:center;letter-spacing:.5px}
.pitch{position:absolute;top:276px;width:100%;text-align:center}
.pitch q{display:block;font-style:italic;font-weight:700;font-size:12px;quotes:"“" "”"}
.pitch p{font-size:10.5px;color:var(--ink-soft);margin-top:3px}
.pillars{position:absolute;left:12px;top:321px;width:441px;height:264px;display:flex;gap:3px}
.pillar{flex:1;background:var(--brand);color:#fff;overflow:hidden}
.pillar h3{height:30px;display:flex;align-items:center;justify-content:center;font-size:10.5px;font-weight:600;border-bottom:1px solid rgba(255,255,255,.7);box-shadow:0 2px 0 rgba(0,0,0,.05)}
.pillar p{padding:10px 8px 0;font-size:8.4px;line-height:1.2;text-align:justify;hyphens:auto}
.promise{position:absolute;top:596px;width:100%;text-align:center}
.promise h4{font-size:11.5px;font-weight:700}
.promise p{font-size:11px;font-style:italic;margin-top:2px}

/* back */
.brand-side{position:absolute;left:8px;top:58px;width:110px;display:flex;flex-direction:column;align-items:center;gap:6px}
.brand-side .mark{width:30px;height:30px;border-radius:50%;background:var(--brand)}
.section-title{text-align:center;font-weight:700;font-size:13.5px;color:var(--brand)}
.divider{display:flex;align-items:center;justify-content:center;gap:6px;margin-top:8px}
.divider span{width:36px;height:1px;background:var(--brand)}
.divider i{width:12px;height:12px;border-radius:50%;background:var(--brand)}
.about__head{position:absolute;left:170px;top:48px;width:200px}
.about__lede{position:absolute;left:126px;top:106px;width:326px;font-size:6.9px;line-height:1.3;color:var(--ink-soft)}
.about__body{position:absolute;left:16px;top:148px;width:436px;height:150px;font-size:6.9px;line-height:1.3;color:var(--ink-soft);overflow:hidden}
.team{position:absolute;left:0;top:307px;width:100%;height:223px;background:var(--brand);color:#fff}
.team .section-title{color:#fff;margin-top:14px}
.team .divider span,.team .divider i{background:#fff}
.portrait{position:absolute;left:18px;top:76px;width:88px;height:110px;border-radius:18px 18px 0 0;background:linear-gradient(180deg,#d9dfe2,#9aa6ab 60%,#2a2f33)}
.team__bio{position:absolute;left:118px;top:66px;width:334px}
.team__bio h5{font-size:8.5px;font-weight:700}
.team__bio small{display:block;font-size:5.8px;margin-top:2px}
.team__bio p{font-size:7.2px;line-height:1.33;margin-top:9px;text-align:justify}
.contact{position:absolute;left:0;top:530px;width:100%;height:105px;background:var(--night);color:#fff;display:flex;justify-content:space-between;padding:26px 28px 0 38px}
.contact__col{display:flex;flex-direction:column;align-items:center;width:118px}
.contact__col h6{font-size:11.5px;font-weight:700;white-space:nowrap}
.contact__btn{margin-top:10px;width:102px;height:25px;border:1.5px solid #fff;display:flex;align-items:center;justify-content:center;font-size:11.5px;font-weight:700}
.contact__phone{margin-top:14px;font-size:11.5px;font-weight:700;white-space:nowrap}
.contact__col small{font-size:5.8px;margin-top:6px;white-space:nowrap}
</style>
</head>
<body>

<section class="sheet sheet--front">
  <div class="topbar">
    <svg width="8" height="8" viewBox="0 0 10 10"><path d="M2 1l2 2-1 1.5c.6 1.2 1.3 1.9 2.5 2.5L7 6l2 2-1.5 1.5C4.5 9.5.5 5.5.5 2.5z" fill="#fff"/></svg>
    <svg width="8" height="6" viewBox="0 0 10 7"><rect width="10" height="7" fill="#fff"/><path d="M0 0l5 4 5-4" stroke="var(--brand)" fill="none"/></svg>
    <span>info@corvalosys.co.uk</span>
    <span class="dot"></span><span class="dot"></span>
  </div>

  <div class="brand-card">
    <span class="mark"></span>
    <span class="brand-name">Corvalo<br>Crafted Systems</span>
  </div>

  <div class="hero" role="img" aria-label="Photo of miniature figurine engineers working on a circuit board">
    <h1 class="hero__title">Allow us to introduce Corvalo Crafted Systems<br>Solutions unique Support service.</h1>
    <div class="hero__tag">SUPPORT</div>
  </div>

  <div class="pitch">
    <q>Providing a cost-effective consultation, design and support service.</q>
    <p>Working with you to meet your ever changing technology requirements.</p>
  </div>

  <div class="pillars">
    <article class="pillar">
      <h3>COST-EFFECTIVE</h3>
      <p>We understand that no matter how small your problem may be or how big a solution you need, price is an important factor. We listen to our clients' needs and expectations, we answer your queries and we build up a dedicated package for you. No added extras, no gimmicks, just a solution. We are bespoke, that's what we do!</p>
    </article>
    <article class="pillar">
      <h3>EXPERIENCED</h3>
      <p>With over 10 years of technology experience and training provided by some of the market leading names; Brightwire Telecom, Kestrel, Ironhat and Quillsoft. Take the top line training and add it to a career employing and developing these skills as a Coastal Fleet Engineer and you get a technician and consultant who lives and breaths technology. Technology changes and advances and so does our training, we continually train and develop our staff so we can better meet, understand and support your demands and needs.</p>
    </article>
    <article class="pillar">
      <h3>PROFESSIONAL</h3>
      <p>It's your home, it's your office – when you invite us to work with you on your bespoke solution, you will receive a professional experience; from the first phone call through to the on-going support you will receive. When you meet our staff, you will be met with the utmost professionalism. We realise that you may have taken time off for our visit and as such will always endeavour to be there at the agreed time.</p>
    </article>
  </div>

  <div class="promise">
    <h4>Corvalo Crafted Systems Solution's Promise.</h4>
    <p>“Ongoing excellence for all our customers both private and commercial.”</p>
  </div>

  <div class="footer"><span class="rule"></span><span class="dot"></span><span>www.corvalosys.co.uk</span><span class="dot"></span><span class="rule"></span></div>
</section>

<section class="sheet sheet--back">
  <div class="topbar">
    <svg width="8" height="8" viewBox="0 0 10 10"><path d="M2 1l2 2-1 1.5c.6 1.2 1.3 1.9 2.5 2.5L7 6l2 2-1.5 1.5C4.5 9.5.5 5.5.5 2.5z" fill="#fff"/></svg>
    <svg width="8" height="6" viewBox="0 0 10 7"><rect width="10" height="7" fill="#fff"/><path d="M0 0l5 4 5-4" stroke="var(--brand)" fill="none"/></svg>
    <span>info@corvalosys.co.uk</span>
    <span class="dot"></span><span class="dot"></span>
  </div>

  <div class="brand-side">
    <span class="mark"></span>
    <span class="brand-name">Corvalo<br>Crafted Systems</span>
  </div>

  <div class="about__head">
    <h2 class="section-title">ABOUT US</h2>
    <div class="divider"><span></span><i></i><span></span></div>
  </div>

  <p class="about__lede">Welcome to Corvalo Crafted Systems Ltd, a professional company formed to meet your demands and exceed your expectations. From the smallest to the most complex technological need; from home computer troubleshooting to a custom designed and fitted tech solution – we are here to support you. Passion, the backbone of our business, and the reason we exist.</p>

  <div class="about__body">
    <p>Formed in 2015 to meet the ever-changing demands of our clients, to infuse our passion for technology with the on-going desire for supporting our clients' needs. We will take the formation of an idea, create a concept and work with our clients in realising that idea. At Corvalo, we realise that our clients' needs are ever changing and we look forward to supporting you every step of the way.</p>
    <p>We enforce three key requirements for our day-to-day business with you, our clients. These are:</p>
    <p>Cost-Effective: We understand that no matter how small your problem may be or how big a solution you need, price is an important factor. We listen to our clients' needs and expectations, we answer your queries and we build up a dedicated package for you. No added extras, no gimmicks, just a solution. We are bespoke, that's what we do.</p>
    <p>Experienced: With over 10 years of technology experience and training provided by some of the market leading names; Brightwire Telecom, Kestrel, Ironhat and Quillsoft. Take the top line training and add it to a career employing and developing these skills as a Coastal Fleet Engineer and you get a technician and consultant who lives and breaths technology. Technology changes and advances and so does our training, we continually train and develop our staff so we can better meet, understand and support your demands and needs.</p>
    <p>Professional: It's your home, it's your office – when you invite us to work with you on your bespoke solution, you will receive a professional experience; from the first phone call through to the on-going support you will receive. When you meet our staff, you will be met with the utmost professionalism. We realise that you may have taken time off for our visit and as such will always endeavour to be there at the agreed time.</p>
  </div>

  <div class="team">
    <h2 class="section-title">OUR TEAM</h2>
    <div class="divider"><span></span><i></i><span></span></div>
    <div class="portrait" role="img" aria-label="Portrait photo of the company director"></div>
    <div class="team__bio">
      <h5>Ewan Marlowe</h5>
      <small>Director and Tech Specialist</small>
      <p>Firstly let me thank you for visiting us here at Corvalo. Corvalo and our team was formed upon recognition of the lack of truly bespoke, all-inclusive tech support in the west of Scotland. I aim to remedy that! I have always had a love for IT and Communications and have completed certified training with Kestrel, Ironhat and Quillsoft, three of the main players in the IT market. In addition to my IT training is time served with Brightwire Telecom and ultimately 10 years with the Coastal Fleet as a Radio and Communications Engineer, working on some of the most complex and advanced communications equipment available. I have a passion for Technology, one that has driven a career and a learning and development platform; a passion that I want to invest with you in making your tech needs happen.</p>
    </div>
  </div>

  <div class="contact">
    <div class="contact__col">
      <h6>CONTACT US ON:</h6>
      <div class="contact__btn">FRIENDWALL</div>
      <small>www.friendwall.com/corvalosys</small>
    </div>
    <div class="contact__col">
      <h6>CALL US ON:</h6>
      <div class="contact__phone">UK: 07700 900418</div>
    </div>
    <div class="contact__col">
      <h6>CONTACT US ON:</h6>
      <div class="contact__btn">CHIRPLINE</div>
      <small>chirpline.com/corvalosysLTD</small>
    </div>
  </div>

  <div class="footer"><span class="rule"></span><span class="dot"></span><span>www.corvalosys.co.uk</span><span class="dot"></span><span class="rule"></span></div>
</section>

</body>
</html>
```